NORVALE DENTAL *

Target Market(s)

Adults 18-60

Contact Information for Business Card

Website: norvaledentalvlm.com
Phone number 555 304 2796 email: crestdentalvlm@mailbox-example.com
Address:471 S. Holloway rd
Suite#24, TX70000
Dr. Marcus Telfer, DDS

Font styles to use
Sans Serif

Requirements
Must have
• Logo, phone number website, doctor,
• 's name

```html
<!DOCTYPE html>
<html lang="en">
<head>
<meta charset="utf-8">
<title>Norvale Dental – Business Card</title>
<link rel="stylesheet" href="https://fonts.googleapis.com/css2?family=Open+Sans:wght@300;400&display=swap">
<style>
  :root {
    --backdrop: #b4b4b4;
    --card: #ffffff;
    --ink: #3a3a3c;
    --teal: #1b7f98;
    --ring: #4a4a4c;
  }
  * { margin: 0; padding: 0; box-sizing: border-box; }
  html, body {
    width: 1200px; height: 1200px; overflow: hidden;
    background: var(--backdrop);
    font-family: "Open Sans", sans-serif;
  }
  .sheet {
    width: 1200px; height: 1200px;
    display: flex; flex-direction: column; align-items: center; justify-content: center;
    gap: 52px;
  }
  .card {
    position: relative;
    width: 900px; height: 514px;
    background: var(--card);
    box-shadow: 0 6px 18px rgba(0,0,0,0.18);
  }
  .brand {
    position: absolute;
    display: flex; align-items: center; gap: 22px;
    color: var(--ink);
    font-weight: 300;
    letter-spacing: 0.04em;
    white-space: nowrap;
  }
  .brand-dot {
    border: 2px solid var(--ring);
    border-radius: 50%;
    flex: none;
  }
  .card-front .brand { left: 50%; top: 50%; transform: translate(-50%, -50%); font-size: 60px; }
  .card-front .brand-dot { width: 92px; height: 92px; }

  .card-back .brand { left: 56px; top: 120px; font-size: 44px; gap: 16px; }
  .card-back .brand-dot { width: 70px; height: 70px; }

  .divider {
    position: absolute;
    left: 418px; top: 200px;
    width: 3px; height: 250px;
    background: var(--teal);
  }
  .details {
    position: absolute;
    left: 462px; top: 206px;
    color: var(--ink);
  }
  .doctor-name {
    font-size: 40px; font-weight: 400;
    color: var(--teal);
    letter-spacing: 0.04em;
    line-height: 1.05;
    white-space: nowrap;
  }
  .doctor-title {
    font-size: 22px; letter-spacing: 0.12em;
    margin-top: 2px; margin-bottom: 26px;
  }
  .contact-list { list-style: none; }
  .contact-item {
    display: flex; align-items: center; gap: 12px;
    font-size: 23px; letter-spacing: 0.03em;
    line-height: 1.45;
    white-space: nowrap;
  }
  .contact-item svg { width: 22px; height: 22px; flex: none; }
  .contact-web { color: var(--teal); }
</style>
</head>
<body>
<main class="sheet">
  <section class="card card-front" aria-label="Card front">
    <div class="brand">
      <span class="brand-dot"></span>
      <span class="brand-name">NORVALE DENTAL</span>
    </div>
  </section>

  <section class="card card-back" aria-label="Card back">
    <div class="brand">
      <span class="brand-dot"></span>
      <span class="brand-name">NORVALE DENTAL</span>
    </div>
    <div class="divider"></div>
    <div class="details">
      <p class="doctor-name">Dr. Marcus Telfer</p>
      <p class="doctor-title">DDS</p>
      <ul class="contact-list">
        <li class="contact-item">
          <svg viewBox="0 0 24 24" aria-hidden="true"><rect x="6" y="1.5" width="12" height="21" rx="2" fill="none" stroke="#1b7f98" stroke-width="2"/><line x1="10" y1="19" x2="14" y2="19" stroke="#1b7f98" stroke-width="2"/></svg>
          <span>555 304 2796</span>
        </li>
        <li class="contact-item">
          <svg viewBox="0 0 24 24" aria-hidden="true"><rect x="1.5" y="5" width="21" height="14" fill="#1b7f98"/><polyline points="1.5,5 12,13 22.5,5" fill="none" stroke="#fff" stroke-width="1.6"/></svg>
          <span>office@norvaledentalvlm.com</span>
        </li>
        <li class="contact-item contact-web">
          <svg viewBox="0 0 24 24" aria-hidden="true"><g fill="none" stroke="#1b7f98" stroke-width="1.6"><circle cx="12" cy="12" r="10"/><ellipse cx="12" cy="12" rx="4.5" ry="10"/><line x1="2" y1="12" x2="22" y2="12"/><line x1="4" y1="6.5" x2="20" y2="6.5"/><line x1="4" y1="17.5" x2="20" y2="17.5"/></g></svg>
          <span>norvaledentalvlm.com</span>
        </li>
      </ul>
    </div>
  </section>
</main>
</body>
</html>
```